Book cover for book titled The Weary Sailor's Drop Ledger

Need a book cover for a book size 5.25 x 8.
Title: The Weary Sailor's Drop Ledger
Subtitle: 35 Habits Worth Shedding So You Can Build Calmer Days Through a Season of Change
Author: Dr. Harold P. Wingate
Foreword by Lionel Ashworth, Ph.D.
The book cover should be white. I have uploaded 2 photos. The closeup with the hat should go on the front with the text. The one in the chair should go on the back. It will be the only thing on the back.

```html
<!DOCTYPE html>
<html lang="en">
<head>
<meta charset="utf-8">
<title>The Weary Sailor's Drop Ledger — Cover</title>
<link rel="stylesheet" href="https://fonts.googleapis.com/css2?family=Oswald:wght@700&family=Hind:wght@400;500&display=swap">
<style>
  :root {
    --paper: #ffffff;
    --ink: #111111;
    --photo-top: #cdb792;
    --photo-mid: #3a3f4c;
    --photo-base: #15181f;
  }
  html, body {
    margin: 0;
    padding: 0;
    width: 840px;
    height: 1200px;
    overflow: hidden;
    background: var(--paper);
  }
  .cover {
    position: relative;
    width: 840px;
    height: 1200px;
    background: var(--paper);
    color: var(--ink);
    text-align: center;
  }
  .title {
    position: absolute;
    top: 78px;
    left: 0;
    width: 100%;
    margin: 0;
    font-family: "Oswald", "Arial Narrow", sans-serif;
    font-weight: 700;
    text-transform: uppercase;
    line-height: 1;
  }
  .title-lead {
    display: block;
    font-size: 66px;
    letter-spacing: -0.5px;
  }
  .title-main {
    display: block;
    margin-top: 2px;
    font-size: 114px;
    letter-spacing: -1.5px;
    line-height: 1.02;
  }
  .subtitle {
    position: absolute;
    top: 312px;
    left: 130px;
    width: 580px;
    margin: 0;
    font-family: "Hind", "Helvetica Neue", sans-serif;
    font-weight: 400;
    font-size: 28px;
    line-height: 1.22;
  }
  .photo {
    position: absolute;
    top: 416px;
    left: 164px;
    width: 492px;
    height: 648px;
  }
  .byline {
    position: absolute;
    top: 1084px;
    left: 0;
    width: 100%;
    font-family: "Hind", "Helvetica Neue", sans-serif;
  }
  .author {
    margin: 0;
    font-size: 46px;
    font-weight: 400;
    text-transform: uppercase;
    line-height: 1.1;
  }
  .foreword {
    margin: 0;
    font-size: 40px;
    font-weight: 400;
    line-height: 1.1;
  }
</style>
</head>
<body>
  <main class="cover">
    <h1 class="title">
      <span class="title-lead">The Weary Sailor's</span>
      <span class="title-main">Drop Ledger</span>
    </h1>
    <p class="subtitle">35 Habits Worth Shedding So You Can Build Calmer Days Through a Season of Change</p>

    <svg class="photo" viewBox="0 0 492 648" role="img" aria-label="Close-up photograph of the author in a straw hat, tinted glasses, face mask and dark jacket, cut out with brush-stroke edges">
      <defs>
        <linearGradient id="photoTone" x1="0" y1="0" x2="0" y2="1">
          <stop offset="0" stop-color="var(--photo-top)"/>
          <stop offset="0.3" stop-color="var(--photo-mid)"/>
          <stop offset="1" stop-color="var(--photo-base)"/>
        </linearGradient>
      </defs>
      <rect x="0" y="0" width="492" height="648" rx="60" fill="url(#photoTone)"/>
    </svg>

    <div class="byline">
      <p class="author">Dr. Harold P. Wingate</p>
      <p class="foreword">Lionel Ashworth, Ph.D.</p>
    </div>
  </main>
</body>
</html>
```